Pull Up Banner - Recruitment Company

We would like a design for a pull up banner.

For context: we are a recruitment business. We specialise in helping people in healthcare industry to find jobs in Australia.

I have come up with several ideas and text for the banner. Feel free to use the following as you see appropriate:

- Our logo (see attached)
- 'Healthcare Recruitment Agency'
- Some sort of imagine / cartoon of medical professionals (ie. doctor, nurse, physiotherapist, speech pathologist). A cartoon is more friendly than committing to a photo
- 'Empowering your next career move'
- 'Discover tailored opportunities based on your career preferences'
- Dot points (allied health, nursing, medical imaging)
- Contact info at the bottom including our website (www.quellstaffing.com.au, our Instagram handle @quellstaffing, Mobile: XXXX XXX XXX. The title section for contact information could be 'Get in touch:'

Feel free to submit a couple of designs and we can merge aspects that look good on your designs and find the perfect fit.
Thank you
Updates

Hello,

Thank you for your initial submissions to this project. I appreciate the time you've invested.

After reviewing the first attempt, I'd like to share some feedback and initial observations:

- Professionalism and engagement: Is the overall appearance of the banner professional? It's crucial that we have a high-quality design as this will represent our business.

- Image selection: The image (whether cartoon or real people) appears quite generic. Please consider submitting the banner with a few different photos in the middle for us to choose from. Ensure the image is a good fit and not simply a generic stock photo.

- Contact section: Kindly remove the phone number; we no longer wish to include it on the banner. Instead, please include our website (www.quellstaffing.com.au) and Instagram handle (@quellstaffing).

- Color scheme: White, black, and red/pink are preferred, or alternatively, blue. However, please avoid incorporating too many different colors as it may detract from the professional appearance.

We will be printing the design on a banner and require it to look professional and engaging.

Thank you once again for your submissions. I hope the feedback provided above is helpful.

Warm regards,

Target Market(s)

Allied Health Australia

Font styles to use
Serif

Colors
0054AA
0677BA
7BADD7
CADEEF
E8F1F8
0094D4
00A9DD
6FCCEA
C7EBF8
E9F6FB
EB3D1F
EC4F4E
F09395
F8D3D4
FCEDEE

```html
<!DOCTYPE html>
<html lang="en">
<head>
<meta charset="utf-8">
<title>Quell Staffing – Pull Up Banner</title>
<link rel="stylesheet" href="https://fonts.googleapis.com/css2?family=Exo+2:ital,wght@0,600;0,800;1,300;1,600;1,700&display=swap">
<style>
  :root{
    --stage:#ececec;
    --paper:#ffffff;
    --rail:#e3e3e3;
    --ink:#111111;
    --brand-blue:#0a70b6;
    --deep-blue:#075a96;
    --sky:#00a9dd;
    --sky-light:#c7ebf8;
    --red:#e8391d;
    --orange:#f28a1e;
    --gold:#e9c31c;
    --white:#ffffff;
  }
  html,body{margin:0;padding:0;width:950px;height:1200px;overflow:hidden;background:var(--stage);}
  .canvas{position:relative;width:950px;height:1200px;}
  .banner{position:absolute;left:212px;top:15px;width:526px;height:1171px;display:block;
    box-shadow:0 14px 30px rgba(0,0,0,.18);}
  .brand-name{font-family:"Exo 2",sans-serif;font-weight:800;font-size:46px;letter-spacing:2px;fill:var(--ink);}
  .headline{font-family:"Exo 2",sans-serif;font-style:italic;font-weight:600;fill:var(--white);}
  .headline--main{font-size:66px;}
  .headline--sub{font-size:52px;}
  .tagline{font-family:"Exo 2",sans-serif;font-style:italic;fill:var(--white);}
  .tagline--lead{font-weight:700;font-size:34px;}
  .tagline--body{font-weight:300;font-size:28px;}
  .field-label{font-family:"Exo 2",sans-serif;font-weight:600;font-size:25px;fill:var(--white);}
  .contact-title{font-family:"Exo 2",sans-serif;font-weight:300;font-size:17px;fill:var(--gold);}
  .contact-text{font-family:"Exo 2",sans-serif;font-weight:600;font-size:22px;fill:var(--white);}
  .contact-phone{font-size:27px;letter-spacing:3px;}
  .icon{fill:none;stroke:var(--white);stroke-width:1.8;}
</style>
</head>
<body>
<main class="canvas">
  <svg class="banner" viewBox="0 0 676 1505" xmlns="http://www.w3.org/2000/svg">
    <defs>
      <radialGradient id="skyGlow" cx="0.55" cy="0.2" r="0.8">
        <stop offset="0" stop-color="#e9f6fb"/>
        <stop offset="0.45" stop-color="#6fccea"/>
        <stop offset="1" stop-color="#00aee8"/>
      </radialGradient>
      <linearGradient id="teamTone" x1="0" y1="0" x2="1" y2="0">
        <stop offset="0" stop-color="#7badd7" stop-opacity=".55"/>
        <stop offset="0.5" stop-color="#0677ba" stop-opacity=".45"/>
        <stop offset="1" stop-color="#7badd7" stop-opacity=".55"/>
      </linearGradient>
    </defs>

    <!-- sheet -->
    <rect class="sheet" width="676" height="1505" fill="var(--paper)"/>
    <rect class="top-rail" y="30" width="676" height="12" fill="var(--rail)"/>

    <!-- brand -->
    <text class="brand-name" x="45" y="150">QUELL STAFFING</text>

    <!-- upper accents -->
    <polygon class="accent-stripe" points="0,312 308,224 230,256 0,343" fill="var(--red)"/>
    <polygon class="headline-band" points="0,367 676,112 676,318 0,572" fill="var(--brand-blue)"/>
    <polygon class="band-edge" points="0,572 676,318 676,324 0,578" fill="var(--white)"/>

    <!-- sky field -->
    <polygon class="sky-field" points="0,578 676,324 676,896 0,1150" fill="url(#skyGlow)"/>

    <text class="headline headline--main" x="335" y="345" text-anchor="middle" transform="rotate(-20.7 335 345)">Healthcare</text>
    <text class="headline headline--sub" x="335" y="415" text-anchor="middle" transform="rotate(-20.7 335 415)">Recruitment Agency</text>

    <!-- team illustration area -->
    <g class="team-illustration" role="img" aria-label="Illustration of five healthcare professionals standing in a row: doctors in white coats and nurses in blue scrubs">
      <rect x="45" y="600" width="575" height="305" rx="18" fill="url(#teamTone)"/>
    </g>

    <!-- lower bands -->
    <polygon class="lower-band" points="0,1150 676,896 676,1505 0,1505" fill="var(--brand-blue)"/>
    <polygon class="message-band" points="0,1148 676,896 676,1062 0,1316" fill="var(--red)"/>
    <polygon class="accent-stripe" points="0,1345 305,1255 235,1282 0,1375" fill="var(--red)"/>

    <text class="tagline tagline--lead" x="332" y="1080" text-anchor="middle" transform="rotate(-20.7 332 1080)">Empowering your next career move</text>
    <text class="tagline tagline--body" x="340" y="1122" text-anchor="middle" transform="rotate(-20.7 340 1122)">Discover tailored opportunities based on</text>
    <text class="tagline tagline--body" x="340" y="1160" text-anchor="middle" transform="rotate(-20.7 340 1160)">your career preferences</text>

    <!-- fields -->
    <g class="fields">
      <rect x="385" y="1188" width="246" height="37" rx="18.5" fill="var(--orange)"/>
      <text class="field-label" x="607" y="1216" text-anchor="end">ALLIED HEALTH</text>
      <rect x="437" y="1236" width="194" height="37" rx="18.5" fill="var(--orange)"/>
      <text class="field-label" x="607" y="1264" text-anchor="end">NURSING</text>
      <rect x="337" y="1288" width="294" height="36" rx="18" fill="var(--orange)"/>
      <text class="field-label" x="607" y="1315" text-anchor="end">MEDICAL IMAGING</text>
    </g>

    <!-- contact -->
    <text class="contact-title" x="90" y="1406">Get in touch</text>
    <g class="contact-icons">
      <g class="icon">
        <circle cx="225" cy="1368" r="8"/>
        <ellipse cx="225" cy="1368" rx="3.5" ry="8"/>
        <line x1="217" y1="1368" x2="233" y2="1368"/>
      </g>
      <circle class="icon" cx="225" cy="1397" r="8"/>
      <g class="icon">
        <circle cx="225" cy="1429" r="9"/>
        <path d="M221 1424 q-1 6 8 10 l1.5 -2 l-2.5 -2 l-1.5 1 q-2.5 -1.5 -3.5 -4 l1 -1.5 l-2 -2.5 z" fill="var(--white)" stroke="none"/>
      </g>
    </g>
    <text class="contact-text" x="251" y="1373">www.quellstaffing.com.au,</text>
    <text class="contact-text" x="251" y="1404">@quellstaffing</text>
    <text class="contact-text contact-phone" x="251" y="1438">0000 000 000</text>

    <!-- base -->
    <rect class="base-strip" y="1467" width="676" height="9" fill="var(--deep-blue)"/>
    <rect class="base-foot" y="1476" width="676" height="29" fill="var(--paper)"/>
  </svg>
</main>
</body>
</html>
```